Business Cards and label design needed!

I am a metalsmith, working in sterling silver, brass and moving slowly into adding some gold accent pieces. I also use patinas to add color to brass pieces. The peacock feather is used in my packaging, as both a label and tissue paper. I am attaching what I am currently using, and printing at home, but I need a design that I can have professionally printed. My website is www.willowharborcrafts.com
Target Market(s)
Established Professionals, Independent thinkers, Art donors, Artist supporters
Industry/Entity Type
Jewelry
Contact Information for Business Card
I would like a business card with the basic contact information, including Facebook and Instagram. I currently use a peacock feather and would like to continue that. I like to use turquoise, Tiffany blue and colors in that direction. I am open to other suggestions. I would like to be able to transfer the design to oval labels as well.
Font styles to use
Other font styles liked:
- Garamond or other fonts that have a slight script that is easy to read
Look and feel

```html
<!DOCTYPE html>
<html lang="en">
<head>
<meta charset="utf-8">
<title>Willow Harbor Crafts – Business Card</title>
<link href="https://fonts.googleapis.com/css2?family=Cinzel:wght@400&family=Lato:wght@400&display=swap" rel="stylesheet">
<style>
  :root {
    --page-bg: #3b3b3d;
    --card-white: #ffffff;
    --teal: #12b3b9;
    --teal-deep: #0d9ca2;
    --ink: #2e2e2e;
    --feather-gold: #c9a774;
    --feather-light: #efe3cf;
    --rule-light: rgba(255,255,255,0.75);
  }
  * { margin: 0; padding: 0; box-sizing: border-box; }
  html, body { width: 1200px; height: 782px; overflow: hidden; }
  body {
    background: var(--page-bg);
    display: flex;
    align-items: center;
    justify-content: center;
    gap: 40px;
  }
  .card {
    position: relative;
    width: 540px;
    height: 309px;
    overflow: hidden;
    box-shadow: 0 8px 22px rgba(0,0,0,0.35);
  }

  /* Front */
  .card-front { background: var(--card-white); }
  .feather-art {
    position: absolute;
    left: 24px; top: 20px;
    width: 120px; height: 100px;
    border-radius: 12px;
    background: linear-gradient(135deg, var(--feather-light) 0%, var(--feather-gold) 60%, var(--feather-light) 100%);
  }
  .brand-name {
    position: absolute;
    left: 160px; top: 78px;
    font-family: 'Cinzel', serif;
    font-weight: 400;
    font-size: 24px;
    letter-spacing: 0.5px;
    color: var(--teal);
    white-space: nowrap;
  }
  .contact-name {
    position: absolute;
    left: 160px; top: 136px;
    font-family: 'Cinzel', serif;
    font-size: 17px;
    letter-spacing: 1.5px;
    color: var(--teal);
  }
  .contact-block {
    position: absolute;
    left: 160px; top: 164px;
    font-family: 'Lato', sans-serif;
    font-size: 14px;
    line-height: 20px;
    color: var(--ink);
  }
  .contact-line { display: flex; align-items: center; gap: 6px; }
  .contact-line svg { width: 11px; height: 11px; fill: var(--teal); flex: none; }

  /* Back */
  .card-back { background: var(--teal); }
  .feather-pattern {
    position: absolute; inset: 0;
    background: linear-gradient(135deg, var(--teal) 0%, var(--teal-deep) 100%);
  }
  .back-content {
    position: absolute; inset: 0;
    display: flex; flex-direction: column; align-items: center; justify-content: center;
    color: #fff;
  }
  .back-brand {
    font-family: 'Cinzel', serif;
    font-size: 27px;
    letter-spacing: 0.5px;
    white-space: nowrap;
  }
  .back-url {
    margin-top: 20px;
    font-family: 'Lato', sans-serif;
    font-size: 14px;
    letter-spacing: 0.3px;
  }
  .social-row {
    margin-top: 14px;
    display: flex; align-items: center; gap: 10px;
  }
  .rule { width: 110px; height: 1px; background: var(--rule-light); }
  .social-dot { width: 18px; height: 18px; border-radius: 50%; background: #fff; }
</style>
</head>
<body>
  <section class="card card-front">
    <div class="feather-art" role="img" aria-label="Peacock feather illustration"></div>
    <div class="brand-name">Willow Harbor Crafts</div>
    <div class="contact-name">Marla Quinn</div>
    <div class="contact-block">
      <div class="contact-line">Willow Harbor Crafts</div>
      <div class="contact-line">Cedar Bluff, TX 76410</div>
      <div class="contact-line">
        <svg viewBox="0 0 12 12" aria-hidden="true"><path d="M2.5 1 L4.5 1 L5.3 3.5 L4 4.5 Q5 7 7.5 8 L8.5 6.7 L11 7.5 L11 9.5 Q10.5 11 9 11 Q1 10 1 3 Q1 1.5 2.5 1 Z"/></svg>
        <span>555-318-2704</span>
      </div>
      <div class="contact-line">
        <svg viewBox="0 0 12 12" aria-hidden="true"><path d="M0.5 2.5 H11.5 V9.5 H0.5 Z M1.2 3 L6 6.6 L10.8 3" stroke="#fff" stroke-width="0.8"/></svg>
        <span>studio@willowharborcrafts.com</span>
      </div>
    </div>
  </section>

  <section class="card card-back">
    <div class="feather-pattern" role="img" aria-label="Repeating peacock feather pattern"></div>
    <div class="back-content">
      <div class="back-brand">Willow Harbor Crafts</div>
      <div class="back-url">www.willowharborcrafts.com</div>
      <div class="social-row">
        <span class="rule"></span>
        <span class="social-dot" aria-label="Social profile"></span>
        <span class="social-dot" aria-label="Social profile"></span>
        <span class="rule"></span>
      </div>
    </div>
  </section>
</body>
</html>
```